Kindred Drift is a movement meditation class that will allow you to focus on the unity of mind, breath and body through easy to follow movement sequences.

A innovative approach to meditation

Target Market(s)

community, all ages

Requirements
Must have
• 1page, 1 side flyer

Kindred Drift - The "O" must be in RED as per suggested graphic
Kindred Drift - the wording must flow like water between the hands as per suggested graphic

Preferred colouring Red/Orange/Yellows

Must include text

Sundays
WEEKLY 5pm
Marlow Bend Neighborhood Centre
Level 1 Marlow Bend Library
Pellam St (Opposite Anvil Hotel)
Marlow Bend

$20 admission
$15 concession
Cash only

0472 918 603 - Dean Whitlock

Like Us on Facebook: Kindred Drift - Dean Whitlock
Nice to have
• What to Bring:
Wear Comfortable clothes that you can move in / Bare feet
Yoga mat or big Towel
Bottled water.
Bring a friend!

```html
<!DOCTYPE html>
<html lang="en">
<head>
<meta charset="utf-8">
<title>Kindred Drift – An Innovative Approach to Meditation</title>
<link rel="stylesheet" href="https://fonts.googleapis.com/css2?family=Archivo+Black&family=Arimo:ital,wght@0,400;0,700;1,700&family=Oswald:wght@500;600&family=Fredoka:wght@600;700&display=swap">
<style>
  :root {
    --ink: #3a3a3a;
    --ink-deep: #2b2a22;
    --orange: #f5a41f;
    --red-orange: #e8512a;
    --green-light: #b9dc6a;
    --green-dark: #6fae3a;
    --teal: #6eb2ab;
    --band-line: #f4a51c;
    --band-ink: #34403f;
    --white: #ffffff;
  }
  * { box-sizing: border-box; margin: 0; padding: 0; }
  html, body { width: 926px; height: 1200px; overflow: hidden; background: #ffffff; }
  .flyer { position: relative; width: 926px; height: 1200px; overflow: hidden; font-family: "Arimo", Arial, sans-serif; }

  .backdrop {
    position: absolute; inset: 0 0 146px 0;
    background:
      radial-gradient(ellipse 260px 200px at 880px 60px, rgba(190,215,140,.75), transparent 70%),
      radial-gradient(ellipse 300px 220px at 120px 70px, rgba(200,220,150,.6), transparent 70%),
      radial-gradient(ellipse 200px 160px at 560px 300px, rgba(210,225,160,.55), transparent 70%),
      radial-gradient(ellipse 240px 120px at 330px 1000px, rgba(214,168,130,.45), transparent 70%),
      radial-gradient(ellipse 200px 260px at 860px 900px, rgba(240,242,245,.8), transparent 70%),
      linear-gradient(180deg, #eef0cf 0%, #f2f1de 35%, #e3e6d8 55%, #c4cdc8 72%, #aebab8 100%);
  }

  .headline { position: absolute; left: 0; top: 0; }

  .intro {
    position: absolute; left: 20px; top: 240px; width: 886px;
    text-align: center; font-weight: 700; font-style: italic;
    font-size: 19.5px; line-height: 29px; color: var(--ink-deep);
  }

  .bring { position: absolute; left: 40px; top: 325px; color: var(--red-orange); }
  .bring h2 { font-size: 24px; font-weight: 700; margin-bottom: 18px; }
  .bring ul { list-style: none; font-size: 18px; line-height: 22px; }
  .bring li { margin-bottom: 28px; }

  .art { position: absolute; left: 0; top: 0; }

  .venue-band {
    position: absolute; left: 0; bottom: 0; width: 926px; height: 146px;
    background: var(--teal); border-top: 11px solid var(--band-line);
  }
  .address {
    position: absolute; left: 40px; top: 14px; font-style: normal;
    font-size: 19px; line-height: 26.5px; font-weight: 700; color: var(--band-ink);
  }
  .contact {
    position: absolute; right: 22px; top: 38px; text-align: right;
    font-weight: 700; color: var(--band-ink);
  }
  .contact .phone { font-size: 24px; line-height: 30px; }
  .contact .social { font-size: 21.5px; line-height: 30px; margin-top: 6px; display: flex; align-items: center; justify-content: flex-end; gap: 8px; }
  .social-mark { width: 24px; height: 24px; background: #e0a43a; border-radius: 3px; }
</style>
</head>
<body>
<div class="flyer">
  <div class="backdrop" role="img" aria-label="Soft photograph of meditating hands in a mudra pose above calm water with green bokeh light"></div>

  <svg class="headline" width="926" height="236" viewBox="0 0 926 236">
    <text x="41" y="82" textLength="842" lengthAdjust="spacingAndGlyphs" font-family="Archivo Black, Arial Black, sans-serif" font-size="50" fill="var(--ink)">A INNOVATIVE APPROACH TO</text>
    <text x="50" y="218" textLength="836" lengthAdjust="spacingAndGlyphs" font-family="Archivo Black, Arial Black, sans-serif" font-size="138" fill="var(--orange)">MEDITATION</text>
  </svg>

  <p class="intro">Kindred Drift is a movement&nbsp; meditation class that will allow you to focus on<br>the unity of mind, breath and body through easy to follow movement sequences.</p>

  <section class="bring">
    <h2>What to Bring:</h2>
    <ul>
      <li>Wear Comfortable clothes<br>that you can move in / Bare feet</li>
      <li>Yoga mat or big Towel</li>
      <li>Bottled water.</li>
      <li>Bring a friend!</li>
    </ul>
  </section>

  <svg class="art" width="926" height="1054" viewBox="0 0 926 1054">
    <defs>
      <radialGradient id="badge-green" cx="40%" cy="30%" r="75%">
        <stop offset="0" stop-color="var(--green-light)"/>
        <stop offset="1" stop-color="var(--green-dark)"/>
      </radialGradient>
      <path id="drift-curve" d="M250 965 C 420 820, 560 760, 850 660"/>
    </defs>

    <g class="badge badge-admission" transform="translate(770 455)">
      <circle r="92" fill="var(--white)"/>
      <circle r="92" fill="none" stroke="var(--white)" stroke-width="16" stroke-linecap="round" stroke-dasharray="0 19.27"/>
      <circle r="82" fill="url(#badge-green)"/>
      <circle r="82" fill="none" stroke="var(--green-light)" stroke-width="12" stroke-linecap="round" stroke-dasharray="0 17.17"/>
      <text y="-2" text-anchor="middle" font-family="Oswald, sans-serif" font-weight="600" font-size="58" fill="var(--ink-deep)">$20</text>
      <text y="44" text-anchor="middle" font-family="Oswald, sans-serif" font-weight="500" font-size="36" fill="var(--ink-deep)">Admission</text>
    </g>

    <g class="badge badge-concession" transform="translate(132 718)">
      <circle r="88" fill="var(--white)"/>
      <circle r="88" fill="none" stroke="var(--white)" stroke-width="16" stroke-linecap="round" stroke-dasharray="0 18.43"/>
      <circle r="78" fill="url(#badge-green)"/>
      <circle r="78" fill="none" stroke="var(--green-light)" stroke-width="12" stroke-linecap="round" stroke-dasharray="0 16.33"/>
      <text y="-34" text-anchor="middle" font-family="Oswald, sans-serif" font-weight="500" font-size="21" fill="var(--ink-deep)">concession</text>
      <text y="16" text-anchor="middle" font-family="Oswald, sans-serif" font-weight="600" font-size="48" fill="var(--ink-deep)">$15</text>
      <text y="52" text-anchor="middle" font-family="Oswald, sans-serif" font-weight="500" font-size="30" fill="var(--ink-deep)">Cash only</text>
    </g>

    <g class="schedule" font-family="Fredoka, sans-serif" font-weight="700">
      <text transform="translate(455 482) rotate(-22)" text-anchor="middle" font-size="62" fill="var(--red-orange)">Sundays</text>
      <text transform="translate(478 545) rotate(-20)" text-anchor="middle" font-size="60" fill="var(--red-orange)">WEEKLY</text>
      <text transform="translate(520 618) rotate(-16)" text-anchor="middle" font-size="64" fill="var(--ink-deep)">5pm</text>
    </g>

    <text class="drift-name" font-family="Fredoka, sans-serif" font-weight="600" font-size="56" letter-spacing="6" fill="var(--ink-deep)">
      <textPath href="#drift-curve">KINDRED DRIFT</textPath>
    </text>
  </svg>

  <footer class="venue-band">
    <address class="address">
      Marlow Bend Neighborhood Centre<br>
      Level 1 Marlow Bend Library<br>
      Pellam St (Opposite Anvil Hotel)<br>
      Marlow Bend
    </address>
    <div class="contact">
      <div class="phone">0472 918 603 - Dean Whitlock</div>
      <div class="social"><span class="social-mark"></span><span>Kindred Drift - Dean Whitlock</span></div>
    </div>
  </footer>
</div>
</body>
</html>
```